Spring Football Signups

We need a flyer for spring football signups that highlights the team (Pellham Stormfoxes), the registration, schedules, the information regarding the different opportunities, and the About Us details of the Football Association.

Target Market(s)

Parents of Youth

Requirements
Must have
• Logos and team colors: purple and black

```html
<!DOCTYPE html>
<html lang="en">
<head>
<meta charset="utf-8">
<title>Pellham Stormfoxes Football – Get In The Game</title>
<link rel="stylesheet" href="https://fonts.googleapis.com/css2?family=Alfa+Slab+One&family=Rubik+Dirt&family=Arimo:wght@400;700&display=swap">
<style>
  :root {
    --purple: #6a1fc2;
    --purple-deep: #4a0a8c;
    --white: #ffffff;
    --black: #000000;
    --ink: #111111;
    --ball-dark: #3a1608;
    --ball-mid: #8a3a1a;
  }
  * { box-sizing: border-box; margin: 0; padding: 0; }
  html, body { width: 900px; height: 1200px; overflow: hidden; background: var(--black); }
  .flyer {
    position: relative; width: 900px; height: 1200px; overflow: hidden;
    background: linear-gradient(180deg, #000 0%, #000 58%, #2a0a52 80%, var(--purple-deep) 92%, var(--purple) 100%);
    font-family: "Arimo", Arial, sans-serif; color: var(--ink);
  }
  .hero-ball {
    position: absolute; left: 0; top: 0; width: 340px; height: 250px;
    background: radial-gradient(ellipse 70% 90% at 30% 30%, var(--ball-mid) 0%, var(--ball-dark) 55%, #000 100%);
  }
  .title {
    position: absolute; left: 310px; width: 590px; text-align: center;
    font-family: "Alfa Slab One", Georgia, serif; color: var(--purple);
    -webkit-text-stroke: 3px var(--white); paint-order: stroke fill;
    text-shadow: 3px 3px 0 var(--white), -3px -3px 0 var(--white), 3px -3px 0 var(--white), -3px 3px 0 var(--white);
    letter-spacing: 3px; line-height: 1; font-size: 94px;
  }
  .title--top { top: 22px; }
  .title--bottom { top: 124px; }

  .panel { position: absolute; background: var(--white); border-radius: 4px; }
  .dates { left: 18px; top: 252px; width: 276px; height: 860px; text-align: center; padding-top: 22px; }
  .dates h2 { font-size: 25px; font-weight: 700; line-height: 1.25; margin-bottom: 22px; }
  .date { margin-bottom: 21px; font-weight: 700; font-size: 17px; line-height: 1.3; }
  .date .when { text-decoration: underline; display: block; }
  .reg-head { font-size: 18px; font-weight: 700; border-bottom: 2px solid var(--ink); margin: 4px 10px 22px; padding-bottom: 2px; }
  .reg-block { font-size: 17px; font-weight: 700; line-height: 1.3; margin-bottom: 20px; }
  .reg-block .label { text-decoration: underline; display: block; }

  .main { left: 316px; top: 252px; width: 568px; height: 863px; text-align: center; }
  .headline {
    font-family: "Rubik Dirt", Impact, sans-serif; color: var(--purple);
    font-size: 88px; line-height: 0.8; margin-top: 22px; letter-spacing: 2px;
  }
  .subhead { color: var(--purple); font-weight: 700; font-size: 23px; line-height: 1.32; margin-top: 18px; }

  .marks { position: absolute; top: 250px; left: 0; width: 568px; height: 140px; }
  .mark { position: absolute; top: 0; width: 170px; height: 140px; display: flex; flex-direction: column; align-items: center; justify-content: center; gap: 8px; }
  .mark__dot { width: 62px; height: 62px; border-radius: 50%; background: var(--purple); }
  .mark__name { font-weight: 700; font-size: 15px; color: var(--purple); }
  .mark--flag { left: 10px; }
  .mark--tackle { left: 192px; }
  .cheer-art { position: absolute; left: 405px; top: 0; width: 120px; height: 140px;
    background: linear-gradient(180deg, #222 0%, #000 100%); border-radius: 40% 40% 10% 10%; }

  .col { position: absolute; top: 398px; width: 170px; font-weight: 700; font-size: 12px; line-height: 1.3; }
  .col h3 { font-size: 15px; margin-bottom: 16px; line-height: 1.25; }
  .col p { margin-bottom: 14px; }
  .col--flag { left: 12px; }
  .col--tackle { left: 194px; }
  .col--cheer { left: 380px; width: 176px; top: 402px; }
  .fee-big { font-size: 15px; }
  .club-mark { position: absolute; left: 380px; top: 672px; width: 180px; height: 175px;
    display: flex; flex-direction: column; align-items: center; justify-content: center; gap: 10px; }
  .club-mark__dot { width: 96px; height: 96px; border-radius: 50%; background: var(--black); }
  .club-mark__name { font-weight: 700; font-size: 19px; line-height: 1.15; color: var(--purple); }

  .footer { position: absolute; left: 0; top: 1124px; width: 900px; text-align: center;
    color: var(--white); font-weight: 700; font-size: 17px; line-height: 1.28; }
</style>
</head>
<body>
<div class="flyer">
  <div class="hero-ball" role="img" aria-label="Close-up photo of a leather football with white laces"></div>
  <div class="title title--top">PELLHAM</div>
  <div class="title title--bottom">FOOTBALL</div>

  <aside class="panel dates">
    <h2>Other Dates<br>To Know:</h2>
    <div class="date"><span class="when">March 9th</span>Spring Kickoff<br>Festival<br>Riverside Commons</div>
    <div class="date"><span class="when">March 30th</span>Last Day to Sign-Up</div>
    <div class="date"><span class="when">April 1st</span>First Day of Practice</div>
    <div class="date"><span class="when">April 11th &amp; 19th</span>RVFA Weigh-Ins</div>
    <div class="date"><span class="when">April 18th</span>Preseason<br>Kickoff Classic</div>
    <div class="date"><span class="when">April 25th</span>Season Begins</div>
    <div class="reg-head">Regular Registration Info</div>
    <div class="reg-block"><span class="label">LOCATION:</span>Hartwell's Grocery<br>Parking Lot<br>418 W. Elm Street<br>Pellham, Texas 75990</div>
    <div class="reg-block"><span class="label">EVERY SATURDAY</span>Registration is from<br>10:00am - 2:00pm</div>
  </aside>

  <main class="panel main">
    <h1 class="headline">GET IN<br>THE GAME</h1>
    <p class="subhead">Stormfoxes Spring Youth Flag &amp; Tackle<br>Football &amp; Cheer Registration</p>

    <div class="marks">
      <div class="mark mark--flag"><span class="mark__dot"></span><span class="mark__name">PIFA 7on7</span></div>
      <div class="mark mark--tackle"><span class="mark__dot"></span><span class="mark__name">Pellham Stormfoxes</span></div>
      <div class="cheer-art" role="img" aria-label="Silhouette of a leaping cheerleader with pom-poms"></div>
    </div>

    <section class="col col--flag">
      <h3>Youth Flag Football</h3>
      <p>Flag Football for the Little Ones!!</p>
      <p>PIFA offers a<br>Flag Football Program for children in<br>Kindergarten &amp; Pre&#8209;K.</p>
      <p>Flag football is utilized primarily to provide an opportunity to participate and learn the basics of playing football.</p>
      <p>Sign-Up Fees are $50.<br>Per Player.</p>
      <p>Each player will be provided with Jersey, Flag Belts, RVFA League Registration and Insurance.</p>
    </section>

    <section class="col col--tackle">
      <h3>Youth Tackle<br>Football</h3>
      <p>Pellham Independent Football offers (3) Divisions:</p>
      <p>Bantam Division:<br>Grades 1 &amp; 2<br>Minor Division:<br>Grades 3 &amp; 4<br>Major Division:<br>Grades 5 &amp; 6</p>
      <p class="fee-big">Sign-Up Fees are<br>$150.</p>
      <p>Players are provided Jersey, Football Pants, RVFA League</p>
      <p>Registration and Insurance player will be provided with Jersey, Flag Belts, RVFA League Registration and Insurance.</p>
    </section>

    <section class="col col--cheer">
      <h3>Youth Cheerleading</h3>
      <p>PIFA offers an All Ages Welcome Cheerleading Program!!</p>
      <p>Anyone interested in cheerleading can participate and cheer for teams in any division.</p>
      <p>Sign-Ups Fees are $250.</p>
      <p>Cheerleaders are provided with full cheer uniform and pom&#8209;poms.</p>
    </section>

    <div class="club-mark"><span class="club-mark__dot"></span><span class="club-mark__name">Pellham<br>Stormfoxes</span></div>
  </main>

  <footer class="footer">
    Pellham Independent Football Association - PO Box 358 Pellham, Texas 75990<br>
    For More Information Visit Our Website - pellhamfootball.com P.I.F.A. is a proud<br>
    member of Ridgeline Valley Football Association
  </footer>
</div>
</body>
</html>
```